KM Group

We need a new website for our company and since we had a very good work done for our logo in this site, we're back for the entire job.

Our company name is Halvorsen Capital Group. We're adding files of examples of what we have done today. In my opinion we need a more attention lock in the site but yet financial simple work.

Our files (attached) will let you know what we have so far. We need a complete change but the colours should be the same, however you can change them not running away to far from the original, and of course matching with the logo.

We need examples for 3 kind of layouts.

- A HOME welcome layout
- An internal Layout with sidebar
- And internal Layout wide

We can buy image licenses if needed for assets.
Actually there are 5 slide images placed on the Welcome HOME, we need those there, but you can improve with better images to match the new website!!!

Target Market(s)

Clients looking for financial advisers, tax and funds specialist, currency advisers

Industry/Entity Type

Financial

Requirements
Must have
• all the fonts must be in accordance with the financial market sites........the welcome home page must be precise, neat and information accurate........the menu should be elegant........main focus on the Home page, should be also the PRIVATE ACCESS box log in.......

```html
<!DOCTYPE html>
<html lang="en">
<head>
<meta charset="utf-8">
<title>Halvorsen Capital Group</title>
<link href="https://fonts.googleapis.com/css2?family=Montserrat:wght@300;400;500;600&display=swap" rel="stylesheet">
<style>
:root{
  --topbar:#3a2414;
  --page:#eeebe4;
  --orange:#e8782a;
  --tan:#e2d5b5;
  --panel:#2e2e2e;
  --field:#1b1b1b;
  --footer:#1e1e1e;
  --text:#333;
  --muted:#9a9a9a;
  --white:#fff;
  --seal:#c9c4ba;
  --up:#2a8a2a;
  --down:#d02020;
}
*{margin:0;padding:0;box-sizing:border-box}
html,body{width:735px;height:1200px;overflow:hidden}
body{position:relative;background:var(--page);font-family:"Montserrat",sans-serif;font-weight:300;color:var(--text)}
.abs{position:absolute}
.topbar{left:0;top:0;width:735px;height:26px;background:var(--topbar)}
.top-btn{top:8px;height:12px;background:var(--orange);color:var(--white);font-size:5.5px;line-height:12px;padding-left:12px;font-weight:400}
.top-btn::before{content:"";position:absolute;left:3px;top:3px;width:6px;height:6px;border:1px solid var(--white)}
.brand{left:88px;top:30px;width:100px;height:46px}
.brand-mark{position:absolute;left:30px;top:2px;width:20px;height:20px;background:var(--orange)}
.brand-name{position:absolute;left:0;top:32px;width:100px;text-align:center;font-size:6.4px;font-weight:500;color:#222;letter-spacing:.2px}
.nav{top:57px;font-size:8.6px;color:#333;font-weight:400}
.nav span{position:absolute;white-space:nowrap}
.slider{left:80px;top:91px;width:575px;height:259px;background:linear-gradient(180deg,#c6c1bb 0%,#8a8074 45%,#3a3128 80%,#1c1712 100%)}
.caption{left:80px;top:284px;width:575px;height:66px;background:rgba(10,10,10,.72)}
.caption h1{position:absolute;left:16px;top:5px;font-size:18px;font-weight:300;color:var(--white)}
.caption p{position:absolute;left:16px;top:31px;width:290px;font-size:7.6px;line-height:16px;color:#ddd}
.arrow{top:308px;width:20px;height:20px;border-radius:50%}
.welcome-band{left:0;top:378px;width:735px;height:202px;background:var(--tan)}
.welcome{left:80px;top:400px;width:380px}
.welcome h2{font-size:11.5px;font-weight:400;color:var(--orange);margin-bottom:12px}
.welcome p{font-size:7px;line-height:14.6px;color:var(--white);margin-bottom:7px;text-align:justify}
.access{left:472px;top:379px;width:183px;height:201px;background:var(--panel)}
.access h3{position:absolute;left:14px;top:24px;font-size:11px;font-weight:400;color:var(--orange)}
.field{position:absolute;left:14px;width:158px;height:23px;background:var(--field);color:#ddd;font-size:8px;line-height:23px;padding-left:7px;font-weight:400}
.forgot{position:absolute;left:20px;top:110px;font-size:7px;color:#ddd;font-weight:400}
.login{position:absolute;left:47px;top:138px;width:90px;height:20px;background:var(--orange);color:var(--white);font-size:6.5px;line-height:20px;text-align:center;font-weight:500}
.card{top:599px;width:185px;height:208px;background:var(--white);border-bottom:3px solid #d8d5cf;box-shadow:0 0 2px rgba(0,0,0,.1)}
.card h4{position:absolute;left:11px;top:6px;font-size:10.6px;font-weight:400;color:var(--orange)}
.card .media{position:absolute;left:8px;top:26px;width:168px;height:75px}
.card p{position:absolute;left:8px;top:112px;width:168px;font-size:7px;line-height:13.5px;color:var(--muted);text-align:justify;letter-spacing:.2px}
.seal{top:846px;height:28px;background:var(--seal)}
.ticker{left:0;top:906px;width:735px;height:32px;background:#f5f5f3;font-size:6.2px;font-weight:600;color:#223;line-height:32px}
.ticker span{position:absolute;white-space:nowrap}
.up{color:var(--up)}.down{color:var(--down)}
.footer{left:0;top:939px;width:735px;height:261px;background:var(--footer)}
.col{top:966px}
.col h5{font-size:10.6px;font-weight:400;color:var(--orange);margin-bottom:8px}
.col li{list-style:none;font-size:7.2px;color:#e6e6e6;line-height:20.8px;font-weight:400}
.divider{left:0;top:1149px;width:735px;height:1px;background:#2c2c2c}
.copy{left:276px;top:1170px;font-size:7.2px;color:#ddd;font-weight:400}
.social{top:1161px;width:17px;height:17px;border-radius:50%;background:var(--white)}
</style>
</head>
<body>
<div class="abs topbar"></div>
<div class="abs top-btn" style="left:541px;width:46px">Apply Now</div>
<div class="abs top-btn" style="left:600px;width:54px">Contact Us</div>

<div class="abs brand">
  <div class="brand-mark"></div>
  <div class="brand-name">HALVORSEN CAPITAL GROUP</div>
</div>

<nav class="abs nav">
  <span style="left:301px">Home</span>
  <span style="left:344px">About Us</span>
  <span style="left:400px">Investments</span>
  <span style="left:467px">Funds</span>
  <span style="left:506px">Brokerage</span>
  <span style="left:561px">Exchange</span>
  <span style="left:615px">Accounts</span>
</nav>

<div class="abs slider" role="img" aria-label="City skyline of office towers lit at dusk"></div>
<div class="abs caption">
  <h1>Financial Managment</h1>
  <p>We offer tailored and Flexible Solutions for banking and finanacial management that meets your business's needs</p>
</div>
<svg class="abs arrow" style="left:579px" viewBox="0 0 20 20"><circle cx="10" cy="10" r="10" fill="#e8782a"/><path d="M12 5 7 10l5 5" stroke="#fff" stroke-width="2" fill="none"/></svg>
<svg class="abs arrow" style="left:603px" viewBox="0 0 20 20"><circle cx="10" cy="10" r="10" fill="#fff"/><path d="M8 5l5 5-5 5" stroke="#222" stroke-width="2" fill="none"/></svg>

<div class="abs welcome-band"></div>
<section class="abs welcome">
  <h2>Welcome to KM Group</h2>
  <p>Lorem Ipsum is simply dummy text of the printing and typesetting industry. Lorem Ipsum has been the industry's standard dummy text ever since the 1500s, when an unknown printer took a galley of type and scrambled it to make a type specimen book. It has survived not only five centuries, but also the leap into electronic typesetting, remaining essentially unchanged. It was popularised in the 1960s with the release of transfer sheets containing Lorem Ipsum passages, and more recently with desktop publishing software like page layout tools including versions of Lorem Ipsum.</p>
  <p>Lorem Ipsum is simply dummy text of the printing and typesetting industry. Lorem Ipsum has been the industry's standard dummy text ever since the 1500s</p>
</section>
<section class="abs access">
  <h3>Private Access</h3>
  <div class="field" style="top:46px">Access Name</div>
  <div class="field" style="top:79px">Access Password</div>
  <div class="forgot">Forgot access name /Password ?</div>
  <div class="login">LOGIN INTO ACCOUNT</div>
</section>

<article class="abs card" style="left:80px">
  <h4>Management &amp; Strategy</h4>
  <div class="media" role="img" aria-label="Hand with pen over financial charts and calculator" style="background:linear-gradient(135deg,#f4f4f2,#d9dcd6 60%,#b8c98a)"></div>
  <p>Lorem Ipsum is simply dummy text of the printing and typesetting industry. Lorem Ipsum has been the industry's standard dummy text ever since the 1500s, when an unknown printer took a galley of type and scrambled ...</p>
</article>
<article class="abs card" style="left:275px">
  <h4>Funds</h4>
  <div class="media" role="img" aria-label="Blue stock market price board" style="background:linear-gradient(135deg,#8fb4de,#3c79c2 55%,#1f4f94)"></div>
  <p>Lorem Ipsum is simply dummy text of the printing and typesetting industry. Lorem Ipsum has been the industry's standard dummy text ever since the 1500s, when an unknown printer took a galley of type and scrambled ...</p>
</article>
<article class="abs card" style="left:471px">
  <h4>Currency Exchange</h4>
  <div class="media" role="img" aria-label="Green buy key and red sell key on a keyboard" style="background:linear-gradient(90deg,#3f8a2c 0%,#4c9a34 48%,#b81818 52%,#c42020 100%)"></div>
  <p>Lorem Ipsum is simply dummy text of the printing and typesetting industry. Lorem Ipsum has been the industry's standard dummy text ever since the 1500s, when an unknown printer took a galley of type and scrambled ...</p>
</article>

<div class="abs seal" style="left:145px;width:64px" role="img" aria-label="Partner seal"></div>
<div class="abs seal" style="left:280px;width:78px" role="img" aria-label="Privacy certification seal"></div>
<div class="abs seal" style="left:415px;width:50px" role="img" aria-label="Trust certification seal"></div>
<div class="abs seal" style="left:517px;width:78px" role="img" aria-label="Security certification seal"></div>

<div class="abs ticker">
  <span class="up" style="left:86px">▲</span>
  <span style="left:108px">GBP/UAH = <b class="up">12.65761 ▲</b></span>
  <span style="left:208px">GBP/UGX = <b class="down">4010.06174 ▼</b></span>
  <span style="left:317px">GBP/USD = <b class="up">1.55817 ▲</b></span>
  <span style="left:412px">GBP/UYU = <b class="up">34.36026 ▲</b></span>
  <span style="left:512px">GBP/VEF = <b style="color:#e8a020">0</b></span>
  <span style="left:576px">GBP/VUV = <b class="up">151.</b></span>
</div>

<footer class="abs footer"></footer>
<div class="abs col" style="left:80px"><h5>About Us</h5><ul><li>History</li><li>Expertize</li><li>Identity</li><li>Startegy</li><li>Contact Us</li></ul></div>
<div class="abs col" style="left:165px"><h5>Investments</h5><ul><li>Term Deposits</li><li>Management &amp; Strategy</li><li>Client Relations</li><li>Financial Privacy</li><li>Tax Advice</li><li>Wealth Analysis &amp; Financial Planning</li></ul></div>
<div class="abs col" style="left:312px"><h5>Overview</h5><ul><li>Administration</li><li>Funds Security</li><li>Core Services</li><li>Reporting</li><li>Revenue Oppurtunities</li><li>How It Works?</li><li>Glossary</li></ul></div>
<div class="abs col" style="left:410px"><h5>Currency Exchange</h5><ul><li>Foreign Exchange</li><li>Fx Forward</li><li>FX Options</li></ul></div>
<div class="abs col" style="left:410px;top:1070px"><h5>Accounts</h5><ul><li>Apply Now</li><li>Private Access</li></ul></div>
<div class="abs col" style="left:556px"><h5>Brokerage</h5><ul><li>Institutional</li><li>Research</li><li>Trading</li></ul></div>
<div class="abs divider"></div>
<div class="abs copy">Copyright ©2013 Company Name &nbsp; - All areserved</div>
<div class="abs social" style="left:626px"></div>
<div class="abs social" style="left:646px"></div>
</body>
</html>
```